Health product web design

I have two websites that look terrible.  They are both 'bee' products related.  The text and links to pages are correct, I just need change the designs.
We are a health product company that sells a range of health and therapeutic products that come from the beehive; including bee pollen, Royal Jelly and Propolis.
The sites to be designed are not ecommerce sites.  They are more information sites that re-direct to our online store (soon to be redesigned) www.orvandale.com.au
The sites I need revamped are:
www.meadowtonic.com.au
www.tarnwick.com.au
Royal Jelly is a substance made by the worker bees and fed to the Queen Bee.  People take Royal Jelly as it is high in a range of B group vitamins and helps increase energy levels, including sexual stamina.
Propolis is antibacterial, antiviral and has an anesthetic quality.  It is used to put on cuts, burns, sore throats, pimples and mouth & stomach ulcers.  Propolis is collected by bees from the sap of trees and used in the bee hive to sterilise it.
You can read the text (there isnt much) on each site to get an idea of what the products are good for.
The design should be colourful but also communicate credability, trust and a healthy lifestyle with an element of science as the products are sold as health and therapeutic related ie. capsules, liquids, ointments etc.
I am open to questions if you need further information.
Thanks

Target Market(s)
Target market is health supplement buyers 40 - 70 yrs
Industry/Entity Type
Health Product
Requirements
Must have
- Both sites will need a basic logo
Lifestyle images - images of healthy 35ish year old people and/or couples
Nice to have
- Images of bee hives
Close up images of bees, flowers
Images of nature

```html
<!DOCTYPE html>
<html lang="en">
<head>
<meta charset="utf-8">
<title>Meadow Tonic Australia</title>
<link href="https://fonts.googleapis.com/css2?family=Arimo:wght@400;700&family=Parisienne&family=Cormorant+Garamond:wght@500&display=swap" rel="stylesheet">
<style>
  :root {
    --cream: #f6ecd6;
    --cream-deep: #e9dcbc;
    --amber: #e0a23a;
    --honey: #f3c75a;
    --rust: #b8470c;
    --tan: #8c7a5b;
    --gold: #a7832f;
    --ink: #222;
    --grey-text: #6f6f6f;
    --panel: #ffffff;
  }
  * { box-sizing: border-box; margin: 0; padding: 0; }
  html, body { width: 1200px; height: 1078px; overflow: hidden; }
  body {
    font-family: "Arimo", Arial, sans-serif;
    color: var(--ink);
    background: linear-gradient(180deg, #fbf6ea 0%, var(--cream) 60%, #f2e3c2 100%);
    position: relative;
  }
  .side-decor {
    position: absolute; top: 0; width: 171px; height: 440px;
    background: radial-gradient(ellipse at 60% 20%, #f7c24d 0%, #d98a1c 30%, rgba(250,240,215,0) 62%),
                radial-gradient(ellipse at 70% 65%, #f1b540 0%, #c97812 24%, rgba(250,240,215,0) 55%);
  }
  .side-decor.left { left: 0; }
  .side-decor.right { right: 0; transform: scaleX(-1); }
  .page {
    position: absolute; left: 171px; top: 0; width: 859px; height: 1078px;
    background: var(--panel);
  }
  .site-header {
    position: absolute; left: 0; top: 0; width: 100%; height: 119px;
    background: linear-gradient(180deg, #fafafa, #ececec);
  }
  .brand {
    position: absolute; left: 52px; top: 36px;
    display: flex; align-items: center; gap: 10px;
  }
  .brand-mark { width: 22px; height: 22px; background: var(--amber); border-radius: 50%; }
  .brand-name {
    font-family: "Cormorant Garamond", Georgia, serif; font-weight: 500;
    font-size: 36px; color: #9a9a9a; letter-spacing: 2px;
  }
  .cert { position: absolute; left: 737px; top: 13px; text-align: center; width: 74px; }
  .cert-badge { width: 48px; height: 48px; border-radius: 50%; border: 3px solid var(--gold); margin: 0 auto; }
  .cert-label { font-size: 11px; color: var(--gold); margin-top: 6px; }
  .main-nav {
    position: absolute; left: 12px; top: 119px; width: 835px; height: 46px;
    background: linear-gradient(180deg, #fff 0%, #f3ead6 100%);
    box-shadow: 0 2px 4px rgba(0,0,0,.12);
    display: flex; align-items: center; font-size: 12px;
  }
  .main-nav a { color: var(--ink); text-decoration: none; position: absolute; top: 15px; }
  .main-nav a.current {
    color: var(--rust); background: #ebebeb; padding: 6px 20px; top: 10px;
  }
  .hero {
    position: absolute; left: 32px; top: 179px; width: 798px; height: 348px;
    border: 2px solid #e4e4e4;
    background: radial-gradient(ellipse at 78% 55%, #e59a1e 0%, #f1c042 22%, rgba(255,240,190,0) 48%),
                radial-gradient(ellipse at 38% 50%, #fbe38a 0%, #fdf0bd 35%, #fffdf6 70%);
  }
  .hero-title { position: absolute; left: 44px; top: 22px; font-family: "Parisienne", cursive; font-size: 78px; color: #c2b28a; }
  .hero-title span { color: var(--rust); }
  .hero-tagline { position: absolute; left: 30px; top: 250px; font-family: "Parisienne", cursive; font-size: 21px; line-height: 29px; color: #333; }
  .section-band {
    position: absolute; left: 32px; top: 533px; width: 798px; height: 44px;
    background: linear-gradient(180deg, #fbf7ee, var(--cream-deep));
  }
  .section-band h1 {
    font-family: "Parisienne", cursive; font-weight: 400; font-size: 34px; color: #4a3f33;
    position: absolute; left: 18px; top: 2px;
  }
  .intro { position: absolute; left: 43px; top: 591px; width: 786px; font-size: 11px; line-height: 16.3px; }
  .intro p { margin-bottom: 16.3px; }
  .hl { color: var(--rust); font-weight: 700; }
  .product-shot {
    position: absolute; left: 53px; top: 848px; width: 85px; height: 133px; border-radius: 10px;
    background: linear-gradient(180deg, #f5f5f5 0%, #ffffff 20%, #f7e04a 30%, #f3cf25 60%, #ffffff 72%, #eeeeee 100%);
  }
  .benefits { position: absolute; left: 182px; top: 843px; width: 660px; }
  .benefits h2 {
    font-family: "Parisienne", cursive; font-weight: 400; font-size: 25px; color: var(--gold);
    padding-bottom: 2px; border-bottom: 1px solid #e3d3aa; width: 300px; margin-bottom: 12px;
  }
  .benefits p { font-size: 11px; line-height: 16.3px; margin-left: 6px; margin-bottom: 16px; }
  .benefits a { display: block; font-size: 11px; font-weight: 700; color: var(--tan); text-decoration: none; margin-left: 6px; margin-bottom: 16px; }
  .site-footer {
    position: absolute; left: 0; top: 1037px; width: 100%; height: 41px;
    background: linear-gradient(180deg, #fff, #dcdcdc);
    font-size: 11px; text-align: right; padding: 12px 17px 0 0;
  }
</style>
</head>
<body>
  <div class="side-decor left" role="img" aria-label="Golden gel capsules decoration"></div>
  <div class="side-decor right" role="img" aria-label="Golden gel capsules decoration"></div>
  <div class="page">
    <header class="site-header">
      <div class="brand"><span class="brand-mark"></span><span class="brand-name">Meadow Tonic</span></div>
      <div class="cert"><div class="cert-badge"></div><div class="cert-label">Halal Certified</div></div>
    </header>
    <nav class="main-nav">
      <a class="current" href="#" style="left:20px">Home</a>
      <a href="#" style="left:112px">Whate is Royal Jelly</a>
      <a href="#" style="left:251px">Benifits Royal Jelly</a>
      <a href="#" style="left:399px">Is Royal Jelly Safe?</a>
      <a href="#" style="left:540px">How is Royal Jelly Collected?</a>
      <a href="#" style="left:735px">Contact Us</a>
    </nav>
    <section class="hero" role="img" aria-label="Royal jelly capsules, honey jar, honeycomb and blossom branch">
      <div class="hero-title">Royal <span>Jelly</span></div>
      <div class="hero-tagline">Lorem Ipsum is simply dummy text of the<br>printing and typesetting industry</div>
    </section>
    <div class="section-band"><h1>Meadow Tonic Australia</h1></div>
    <main class="intro">
      <p><span class="hl">Royal Jelly</span> is a power pack of nutrition, designed by nature to create the queen bee and used by humans to maintain maximum health. Traditionally recognised for its ability to increase vitality, improve digestion and condition the skin, hair and nails, new benefits of taking Royal Jelly, such as improved liver function, reliev-ing stress, lowering cholesterol, and anti-inflammatory and anti-bacterial properties, are also being discovered.</p>
      <p><span class="hl">Purehive™ Royal Jelly</span> products include fresh Royal Jelly (250gm / 1kg), and Royal Jelly gel capsules (60 / 365 caps). Purehive™ Royal Jelly and Purehive™ Propolis products are selected from the purest beehives – free from chemical or antibiotic sprays. You can purchase <span class="hl">Purehive™ Royal Jelly</span> from our online store or from one of our trusted suppliers.</p>
      <p>While all bee larvae are fed <span class="hl">Royal Jelly</span> in their first few days, a select few larva are fed generous quantities of Royal Jelly for their first four days.</p>
      <p>These larger servings of <span class="hl">Royal Jelly</span> set off a cascade of events within the larva that result in the development of ovaries – and a new queen is born.</p>
      <p>While the worker bee is destined to a short, seven or eight-week life of hard work, the queen bee will eat nothing but <span class="hl">Royal Jelly</span> for the rest of her life, ensuring that her reign, of five to seven years, is long and productive.</p>
    </main>
    <div class="product-shot" role="img" aria-label="Tub of fresh royal jelly"></div>
    <section class="benefits">
      <h2>Multitude of health benefits</h2>
      <p>Like other bee propolis products, such as Propolis and honey, Royal Jelly is believed to have a multitude of health benefits for humans – royal or otherwise.</p>
      <a href="#">Buy Royal Jelly Online</a>
      <a href="#">Australian Royal Jelly</a>
    </section>
    <footer class="site-footer">(c) Copyright Meadow Tonic Australia 2011</footer>
  </div>
</body>
</html>
```